Hollis Ironworks Business Card

We need a business card design for a new small metal fabrication business in rural NSW, Australia.

The business (Hollis Ironworks) is owner operated by a man with the initials RB - much of the branding comes from this name.

Hollis Ironworks designs, engineers, repairs and manufactures a range of custom, quality metal works including vehicle trays, agricultural machinery impliments, trailers, wood splitters, fire pits, furniture etc.

The brand position focuses on custom work of the highest quality.

Business card design should show quality, attention to detail and stand out among a mass of business cards.

Logos are in the files

The grey color may be changed on the logo if required to stand out more.

There is an image attached of a simple card that is liked because it is clean, clear, simple, masculine and effective. It says 'quality'. As most of the work we do is custom it would be good to have the business card speak to this.

Target Market(s)

Rural and regional based Australians. Primarily adult male 25-60 yrs. Primary production / rural / travelling lifestyle.

Industry/Entity Type

Metal Fabrication

Contact Information for Business Card

The words 'custom quality fabrications' would be great somewhere perhaps on the backside (not on the information side)
Name
title
Phone: 0491 538 274 and (02) 7342 9185
email: info@hollisiw.com.au
www.hollisiw.com.au

address (2 lines)

Requirements
Nice to have
• Background colour should be very navy blue or black.
Should not have
• NO orange and blue combinations.
• Navy is OK

```html
<!DOCTYPE html>
<html lang="en">
<head>
<meta charset="utf-8">
<title>Hollis Ironworks Business Card</title>
<link href="https://fonts.googleapis.com/css2?family=Saira:wght@300;400;600;700&display=swap" rel="stylesheet">
<style>
  :root {
    --backdrop: #b9b9b9;
    --card: #f3f3f3;
    --card-white: #fafafa;
    --green: #6cc04a;
    --charcoal: #4d4d4d;
    --charcoal-dark: #3d3d3d;
    --logo-grey: #8c8c8c;
    --ink: #333333;
    --muted: #8a8a8a;
  }
  * { box-sizing: border-box; margin: 0; padding: 0; }
  html, body {
    width: 1200px; height: 900px; overflow: hidden;
    background: var(--backdrop);
    font-family: "Saira", sans-serif;
  }
  .sheet {
    position: relative; width: 1200px; height: 900px;
  }
  .card {
    position: absolute; left: 340px;
    width: 520px; height: 316px;
    box-shadow: 0 6px 18px rgba(0,0,0,0.18);
    overflow: hidden;
  }
  /* Front */
  .card--front {
    top: 100px;
    background: var(--card);
    border-top: 9px solid var(--green);
    border-bottom: 9px solid var(--green);
    display: flex; align-items: center; justify-content: center;
  }
  .brand-name {
    color: var(--logo-grey);
    font-weight: 600;
    font-size: 50px;
    line-height: 1.05;
    letter-spacing: 4px;
    text-transform: uppercase;
    text-align: center;
  }
  /* Back */
  .card--back {
    top: 484px;
    background: var(--card-white);
    display: flex;
  }
  .contact-rail {
    width: 104px; height: 100%;
    display: flex; flex-direction: column;
  }
  .rail-mark {
    height: 104px; background: var(--charcoal);
    display: flex; align-items: center; justify-content: center;
    color: #ffffff; font-weight: 600; font-size: 38px; letter-spacing: 1px;
  }
  .rail-row {
    display: flex; align-items: center; justify-content: flex-end;
    padding-right: 16px;
    border-right: 1px solid rgba(255,255,255,0.35);
  }
  .rail-row--green { background: var(--green); height: 46px; }
  .rail-row--dark { background: var(--charcoal-dark); height: 28px; }
  .rail-row--fill { flex: 1; background: var(--green); }
  .rail-row svg { width: 22px; height: 22px; fill: var(--charcoal-dark); }
  .details {
    flex: 1; padding: 0 0 0 22px;
    display: flex; flex-direction: column;
  }
  .person { margin-top: 114px; }
  .person-name { font-size: 21px; color: var(--ink); line-height: 1.1; }
  .person-name strong { font-weight: 700; }
  .person-name span { font-weight: 400; }
  .person-title { font-size: 15px; font-weight: 300; color: var(--muted); }
  .contact-lines { margin-top: 40px; font-size: 14px; line-height: 1.35; color: var(--ink); font-weight: 400; }
  .contact-lines .gap { margin-top: 10px; }
</style>
</head>
<body>
<main class="sheet">
  <section class="card card--front" aria-label="Business card front">
    <h1 class="brand-name">Hollis<br>Ironworks</h1>
  </section>

  <section class="card card--back" aria-label="Business card back">
    <div class="contact-rail">
      <div class="rail-mark">RB</div>
      <div class="rail-row rail-row--green">
        <svg viewBox="0 0 24 24" aria-hidden="true"><circle cx="12" cy="7" r="5"/><path d="M2 23c0-6 4.5-9 10-9s10 3 10 9z"/></svg>
      </div>
      <div class="rail-row rail-row--dark"></div>
      <div class="rail-row rail-row--green">
        <svg viewBox="0 0 24 24" aria-hidden="true"><path d="M2 8c0-3 4-5 10-5s10 2 10 5v2h-5V8H7v2H2z"/><path d="M5 12h14l2 9H3z"/></svg>
      </div>
      <div class="rail-row rail-row--dark"></div>
      <div class="rail-row rail-row--fill">
        <svg viewBox="0 0 24 24" aria-hidden="true"><path d="M2 5h20v14H2z" fill="none" stroke="#3d3d3d" stroke-width="2"/><path d="M2 5l10 8 10-8" fill="none" stroke="#3d3d3d" stroke-width="2"/></svg>
      </div>
    </div>
    <div class="details">
      <div class="person">
        <p class="person-name"><strong>Forename</strong> <span>Surname</span></p>
        <p class="person-title">Member of the Board</p>
      </div>
      <div class="contact-lines">
        <p>0491 538 274</p>
        <p>(02) 7342 9185</p>
        <p class="gap">info@hollisiw.com.au</p>
        <p>www.hollisiw.com.au</p>
      </div>
    </div>
  </section>
</main>
</body>
</html>
```